I have a mobile MMO game and I am looking for a talented graphic designer who can do the User Interface design similar to the attached one, in cartoonish style, but not the same please. For this contest, all you need to do is to design two items: the button temple and the resource bar temple. I will reward the best design and also hire him/her for the project. More info about the game: It's a war game in a fantasy world, in which you can build a kingdom and fight with others. You have troops. like dragons, giants, archers, etc.

```html
<!DOCTYPE html>
<html lang="en">
<head>
<meta charset="utf-8">
<title>Button and Resource Bar Templates</title>
<link rel="stylesheet" href="https://fonts.googleapis.com/css2?family=Open+Sans:wght@700;800&display=swap">
<style>
  :root {
    --canvas-bg: #ffffff;
    --label-white: #ffffff;
    --bar-outline: #231f20;

    --red-strip: #8e1c5e;
    --red-border: #e3262e;
    --red-top: #fcc9cc;
    --red-mid: #f58489;
    --red-base: #ec2a32;
    --red-deep: #d71920;
    --red-shadow: rgba(190, 20, 30, 0.55);
    --red-bar-start: #9a1f6b;
    --red-bar-mid: #e0303e;
    --red-bar-end: #f26a22;

    --grey-strip: #231f20;
    --grey-border: #1c1a1b;
    --grey-top: #c8c8c9;
    --grey-mid: #a3a3a5;
    --grey-base: #6d6e70;
    --grey-deep: #3f3f41;
    --grey-shadow: rgba(20, 20, 20, 0.5);
    --grey-bar-start: #231f20;
    --grey-bar-mid: #6f7073;
    --grey-bar-end: #ffffff;

    --green-strip: #0c6a36;
    --green-border: #0e8c43;
    --green-top: #c5e8cf;
    --green-mid: #7fcb95;
    --green-base: #2fae56;
    --green-deep: #10913f;
    --green-shadow: rgba(16, 140, 64, 0.5);
    --green-bar-start: #0b6636;
    --green-bar-mid: #0b9444;
    --green-bar-end: #3fb74c;
  }

  * { margin: 0; padding: 0; box-sizing: border-box; }

  html, body {
    width: 1200px;
    height: 848px;
    overflow: hidden;
    background: var(--canvas-bg);
  }

  .canvas {
    position: relative;
    width: 1200px;
    height: 848px;
  }

  .ui-set {
    position: absolute;
    left: 0;
    width: 1200px;
    height: 152px;
  }
  .ui-set--red { top: 101px; }
  .ui-set--grey { top: 328px; }
  .ui-set--green { top: 555px; }

  .button-backplate {
    position: absolute;
    left: 84px;
    top: 22px;
    width: 423px;
    height: 111px;
  }

  .game-button {
    position: absolute;
    left: 107px;
    top: 0;
    width: 378px;
    height: 152px;
    border-radius: 8px;
    border: 3px solid;
    display: flex;
    align-items: center;
    justify-content: center;
    overflow: hidden;
  }

  .game-button::before {
    content: "";
    position: absolute;
    left: 0; right: 0; top: 0;
    height: 48%;
    background: linear-gradient(to bottom, rgba(255,255,255,0.35), rgba(255,255,255,0.1));
  }

  .game-button__label {
    position: relative;
    font-family: "Open Sans", sans-serif;
    font-weight: 700;
    font-size: 80px;
    letter-spacing: 0.5px;
    color: var(--label-white);
    line-height: 1;
    margin-top: 2px;
  }

  .resource-bar {
    position: absolute;
    left: 516px;
    top: 22px;
    width: 599px;
    height: 111px;
    border: 1.5px solid var(--bar-outline);
  }

  /* Red set */
  .ui-set--red .button-backplate { background: var(--red-strip); }
  .ui-set--red .game-button {
    border-color: var(--red-border);
    background: linear-gradient(to bottom, var(--red-top) 0%, var(--red-top) 30%, var(--red-mid) 52%, var(--red-base) 75%, var(--red-deep) 100%);
    box-shadow: 0 8px 10px -2px var(--red-shadow);
  }
  .ui-set--red .resource-bar {
    background: linear-gradient(70deg, var(--red-bar-start) 0%, var(--red-bar-mid) 60%, var(--red-bar-end) 100%);
  }

  /* Grey set */
  .ui-set--grey .button-backplate { background: var(--grey-strip); }
  .ui-set--grey .game-button {
    border-color: var(--grey-border);
    background: linear-gradient(to bottom, var(--grey-top) 0%, var(--grey-top) 30%, var(--grey-mid) 52%, var(--grey-base) 78%, var(--grey-deep) 100%);
    box-shadow: 0 8px 10px -2px var(--grey-shadow);
  }
  .ui-set--grey .resource-bar {
    background: linear-gradient(70deg, var(--grey-bar-start) 0%, var(--grey-bar-mid) 60%, var(--grey-bar-end) 100%);
  }

  /* Green set */
  .ui-set--green .button-backplate { background: var(--green-strip); }
  .ui-set--green .game-button {
    border-color: var(--green-border);
    background: linear-gradient(to bottom, var(--green-top) 0%, var(--green-top) 30%, var(--green-mid) 52%, var(--green-base) 75%, var(--green-deep) 100%);
    box-shadow: 0 8px 10px -2px var(--green-shadow);
  }
  .ui-set--green .resource-bar {
    background: linear-gradient(70deg, var(--green-bar-start) 0%, var(--green-bar-mid) 55%, var(--green-bar-end) 100%);
  }
</style>
</head>
<body>
  <main class="canvas">
    <section class="ui-set ui-set--red">
      <div class="button-backplate"></div>
      <div class="game-button"><span class="game-button__label">BUTTON</span></div>
      <div class="resource-bar"></div>
    </section>

    <section class="ui-set ui-set--grey">
      <div class="button-backplate"></div>
      <div class="game-button"><span class="game-button__label">BUTTON</span></div>
      <div class="resource-bar"></div>
    </section>

    <section class="ui-set ui-set--green">
      <div class="button-backplate"></div>
      <div class="game-button"><span class="game-button__label">BUTTON</span></div>
      <div class="resource-bar"></div>
    </section>
  </main>
</body>
</html>
```